Ferncastle Postgraduate Fellows' Circle Annual Symposium Poster

We need a poster to advertise for our annual symposium. The poster will be printed on 11X17" paper.

Our organization is the Ferncastle Postgraduate Fellows' Circle. Our logo is in the uploaded files.

The title of this year's symposium is "Tidewater Notes - Echoes of the Orchard." The Symposium will take place on March 31, 2017 in KW - 42.

We are accepting papers on the topics of Canada and the world; Indigenous politics in Canada; Canadian national identity; Race, racialization and belonging; Gender and politics in Canada; Queer politics and sexualities; Class and labour politics in Canada; Environmental politics; Canadian government and politics.

There will be a lunch hour roundtable discussion on the topic of "Decolonizing the Discipline of Political Science."
Confirmed Speakers include Dr. Corvella Brandt, Dr. Renata Quillfeather-Osorio, Dr. Tobin Veraux, Dr. Hester Dunmore
This round-table will consider questions of Race, Indigeneity, and Ethnicity in Political Science Research and efforts by the universities to "Decolonize," "Indigenize," and "Reconcile" the academy.
The roundtable will take place in KW-42 from 12:00 - 1:00 pm.
Lunch will be provided.

There will be a keynote panel sponsored by the Halvorsen Institute for Civic Shelter Studies on the topic of "Canada’s renewed vision of peacekeeping."
Their logo is in the uploaded files.

For more information and a full schedule or events, visit our website: http://fpfcgathering.tallpine.net/thanks.html

Sponsors should be listed at the bottom of the page: The Faculty of Arts, The Department of Political Science, HICS3

Target Market(s)

University students and staff who may come to the symposium

Industry/Entity Type

Political

Logo Text

FPFC Ferncastle Postgraduate Fellows' Circle

Font styles to use
Sans Serif

Colors
ec1f27
f37122
9bcb3c
ffcf3e

Requirements
Must have
• Coulours/Leaves/etc should match this website:
• http://fpfcgathering.tallpine.net/thanks.html
• Title of Symposium, Date, Room Number
• Sponsor logos at the bottom of the page
• Date/Time for Roundtable
Nice to have
• This list:
• We are accepting papers on the topics of Canada and the world; Indigenous politics in Canada; Canadian national identity; Race, racialization and belonging; Gender and politics in Canada; Queer politics and sexualities; Class and labour politics in Canada; Environmental politics; Canadian government and politics.
• This statement:
• This round-table will consider questions of Race, Indigeneity, and Ethnicity in Political Science Research and efforts by the universities to "Decolonize," "Indigenize," and "Reconcile" the academy.

```html
<!DOCTYPE html>
<html lang="en">
<head>
<meta charset="utf-8">
<title>Tidewater Notes – Echoes of the Orchard</title>
<link href="https://fonts.googleapis.com/css2?family=Oswald:wght@500;700&family=Open+Sans:wght@400;600;700;800&display=swap" rel="stylesheet">
<style>
:root{
  --red:#ec1f27;
  --orange:#f37122;
  --green:#9bcb3c;
  --yellow:#ffcf3e;
  --blue:#1e9ad6;
  --ink:#111111;
  --paper:#ffffff;
  --grey:#444444;
}
*{box-sizing:border-box;margin:0;padding:0}
html,body{width:778px;height:1200px;overflow:hidden;background:var(--paper)}
.poster{position:relative;width:778px;height:1200px;font-family:"Open Sans",Arial,sans-serif;color:var(--ink)}
.date-bar{height:34px;background:var(--red);color:var(--yellow);font-family:"Oswald",Arial,sans-serif;font-weight:700;font-size:22px;text-align:center;line-height:34px;letter-spacing:.5px}
.hero{position:relative;height:396px;background:
  radial-gradient(circle at 20% 30%,#f6a21e 0,transparent 35%),
  radial-gradient(circle at 80% 25%,#d63a1a 0,transparent 35%),
  radial-gradient(circle at 75% 80%,#8fbf35 0,transparent 40%),
  radial-gradient(circle at 15% 80%,#c9261f 0,transparent 40%),
  linear-gradient(135deg,#7a2a14,#b8501c 50%,#5a3a16)}
.org-mark{position:absolute;left:50%;top:120px;transform:translateX(-50%);text-align:center;color:var(--paper);font-family:"Open Sans",Arial,sans-serif;font-weight:800;line-height:1}
.org-mark .acronym{font-size:78px;letter-spacing:2px}
.org-mark .full-name{font-size:19px;margin-top:8px;letter-spacing:.5px}
.title-band{background:var(--ink);height:110px;padding:14px 0 0 38px;font-family:"Oswald",Arial,sans-serif;font-weight:700;text-transform:uppercase;line-height:1.05}
.title-band .presents{color:var(--paper);font-family:"Open Sans",Arial,sans-serif;font-weight:700;font-size:22px;text-transform:none}
.title-band .headline{color:var(--orange);font-size:40px}
.title-band .subline{color:var(--paper);font-size:30px;padding-left:0}
.info{padding:16px 40px 0;height:395px;text-align:center}
.panels h2{font-size:18px;font-weight:800;margin-bottom:8px}
.topics{display:flex;justify-content:center;gap:60px;text-align:left;font-size:15px;font-weight:600;line-height:1.45}
.topics ul{list-style:none}
.topics li::before{content:"• "}
.roundtable{margin-top:14px;font-size:14px;font-weight:700}
.roundtable .speakers{font-size:13px;font-weight:700}
.roundtable .when{color:var(--red);font-family:"Oswald",Arial,sans-serif;font-weight:700;font-size:19px;margin-top:8px}
.roundtable p{font-size:13px;font-weight:600;line-height:1.4;color:var(--grey)}
.keynote{margin-top:14px}
.keynote h3{font-family:"Oswald",Arial,sans-serif;font-size:21px;font-weight:500}
.keynote .sponsor{color:var(--red);font-weight:700;font-size:14px}
.more{margin-top:8px;font-size:13px;font-weight:700}
.more .url{display:block;font-weight:600}
.faces{height:145px;background:linear-gradient(90deg,#6b4a1c,#c48a3a 30%,#e0b060 50%,#b47a32 70%,#5d3f18)}
.sponsors{display:flex;justify-content:center;align-items:center;gap:70px;height:120px}
.sponsor-mark{display:flex;align-items:center;gap:10px;font-weight:700;color:var(--ink)}
.sponsor-mark .square{width:42px;height:42px;background:var(--green)}
.sponsor-mark .name{font-size:13px;line-height:1.2}
.sponsor-mark .name strong{display:block;font-size:26px;font-weight:700}
</style>
</head>
<body>
<div class="poster">
  <header class="date-bar">FRIDAY MARCH 31, 2017 9:00AM-5:00PM IN KW - 42</header>

  <section class="hero" role="img" aria-label="Collage of autumn maple leaves in red, orange, yellow and green with portraits of students">
    <div class="org-mark">
      <div class="acronym">FPFC</div>
      <div class="full-name">FERNCASTLE POSTGRADUATE FELLOWS' CIRCLE</div>
    </div>
  </section>

  <section class="title-band">
    <div><span class="presents">presents: </span><span class="headline">Tidewater Notes</span></div>
    <div class="subline">Echoes of the Orchard.</div>
  </section>

  <main class="info">
    <section class="panels">
      <h2>Student Panel Discussions will consider topics such as:</h2>
      <div class="topics">
        <ul>
          <li>Canada and the world;</li>
          <li>Indigenous politics in Canada;</li>
          <li>Canadian national identity;</li>
          <li>Race, racialization and belonging;</li>
          <li>Gender and politics in Canada;</li>
        </ul>
        <ul>
          <li>Queer politics and sexualities;</li>
          <li>Class and labour politics in Canada;</li>
          <li>Environmental politics; or</li>
          <li>Canadian government and politics.</li>
        </ul>
      </div>
    </section>

    <section class="roundtable">
      <div>Lunchtime Roundtable, "Decolonizing the Discipline," Featuring</div>
      <div class="speakers">DR. CORVELLA BRANDT • DR. RENATA QUILLFEATHER-OSORIO • DR. TOBIN VERAUX • DR. HESTER DUNMORE</div>
      <div class="when">FRIDAY MARCH 31, 2017 12:00-1:00PM IN KW-42 • LUNCH WILL BE PROVIDED.</div>
      <p>This round-table will consider questions of Race, Indigeneity, and Ethnicity in Political Science<br>research and efforts by universities to "Decolonize," "Indigenize," and "Reconcile" the academy.</p>
    </section>

    <section class="keynote">
      <h3>"CANADA'S RENEWED VISION OF PEACEKEEPING"</h3>
      <div class="sponsor">This panel is sponsored by the Halvorsen Institute for Civic Shelter Studies</div>
    </section>

    <div class="more">For more information and a full schedule or events, visit our website:
      <span class="url">http://fpfcgathering.tallpine.net/thanks.html</span>
    </div>
  </main>

  <section class="faces" role="img" aria-label="Strip of close-up portrait photographs of students"></section>

  <footer class="sponsors">
    <div class="sponsor-mark"><span class="square"></span><span class="name"><strong>HICS3</strong>Halvorsen Institute for Civic Shelter Studies</span></div>
    <div class="sponsor-mark"><span class="square"></span><span class="name"><strong>FERNCASTLE UNIVERSITY</strong>FACULTY OF ARTS · Department of Political Science</span></div>
  </footer>
</div>
</body>
</html>
```